Design a Bold Tradeshow Backdrop for a Sustainable Cleaning Technology

We need a professional, high-impact 10' × 8' tradeshow backdrop for Vornelle®, a commercial cleaning technology company. 143.75" x 90" high and needs bleeds in the 143.75" direction for printing but the graphic area is 10' wide.

Our first event will have an audience that includes K–12 school administrators, facility managers, business officials, and custodial decision-makers. However, this backdrop will be used at multiple future trade shows across different commercial and institutional markets.

The design therefore needs to be universal rather than specifically education- or school-themed.

Our goal is to stop attendees as they walk past the booth and immediately communicate a simple message:

Safer and more sustainable cleaning can also cost substantially less than conventional cleaning chemicals.

We want the design to feel modern, innovative, clean, sustainable, credible, commercial, and premium. It should resonate with K–12 decision-makers while being equally appropriate at events serving commercial facilities, healthcare, hospitality, government, property management, transportation, and other institutional markets.

It should NOT look like a traditional janitorial supply advertisement and should not be overly busy.

The most important messages need to be understandable from approximately 10–20 feet away.

Required Messaging

The primary headline should be:

SUSTAINABLE CLEANING
DOES NOT HAVE TO BE EXPENSIVE.

Three major value propositions should be prominently displayed:

FREE
Cleaning Chemical Analysis
See how much you can save.

SAVE UP TO 60% or More
on Cleaning Chemical Costs

AS LITTLE AS $0.27/GALLON

We would also like a strong secondary message incorporated into the design:

SMARTER CLEANING.
High Performance. Low Cost. Safer.

Visual Direction — Important

Rather than showing a K–12 school hallway or other environment that limits the backdrop to the education market, we want a sophisticated, universal commercial or institutional environment.

This could be a bright, contemporary commercial facility, lobby, corridor, office environment, public building, or other premium architectural space that could reasonably represent many different types of facilities.

The environment should communicate:

Cleanliness • Safety • Sustainability • Professionalism • Efficiency • High Performance

We want someone from a school, hospital, hotel, office building, airport, government facility, or other commercial property to be able to look at the backdrop and relate the imagery to their own facility.

Please avoid imagery that makes the backdrop industry-specific.

We also want to avoid clichéd environmental imagery. The design does not need to be covered in leaves, trees, water droplets, recycling symbols, or other obvious "green" graphics to communicate sustainability. We prefer a sophisticated commercial interpretation of sustainability.

Color & Brand Direction

We want the overall color palette to stay primarily within:

Blues — consistent with our corporate identity

Greens — to reinforce sustainability, safety, efficiency, and environmental responsibility

White — strongly encouraged for clean space, contrast, and an open contemporary appearance

Black — should be limited primarily to text where necessary for readability

Please avoid making black a major background or dominant design color.

We want the finished display to have a bright, clean, sophisticated, sustainable look and feel rather than a dark or industrial appearance.

The design should use significant negative space and a strong visual hierarchy.

Less is more.

We prefer a few large, powerful messages that can be understood quickly rather than numerous small bullet points, paragraphs, or icons.

Creative Freedom

The attached concept image is provided to communicate our general direction and messaging only.

It does not need to be copied.

We are specifically running this contest because we want designers to improve upon our initial concept and show us different creative approaches to presenting the Vornelle value proposition.

We are open to creative interpretations of the commercial environment, composition, typography, use of negative space, and how the three major financial benefits are presented.

The finished design should feel like an innovative commercial technology brand, not simply another cleaning chemical company.

Corporate Logo — Very Important

We are attaching our official Vornelle® corporate logo for use in the design.

DO NOT redraw, recreate, modify, stylize, reinterpret, trace, or AI-generate the Vornelle logo.

The supplied corporate logo must be inserted directly into the artwork exactly as provided, maintaining its original proportions, colors, typography, trademark elements, and graphic design.

The logo should generally appear in the upper-left area of the backdrop but should not overwhelm the primary marketing message.

Printer Template & Graphic Sizing

We are also attaching the printer's official graphic template and instructions for the 8' × 8' tension-fabric display.

Designers should create their artwork using these supplied specifications so the winning design can be transferred directly into production.

The printer requires that the original document size not be changed, artwork be created on the designated design layer or a new layer, images be embedded, text be converted to outlines, and the finished production artwork be supplied as a PDF.

Please pay particular attention to the bleed area, finished size, and safe artwork area when positioning important text, graphics, and the corporate logo.

Physical Booth Context

The backdrop will sit behind an 8' tradeshow table.

The complete booth will also contain:

A blue stretch tablecloth with the Vornelle corporate logo
BrevoMax and Vornelle product containers and samples on the table
An HulaDrent chemical mixing/dilution station displayed on an elevated stand to the left
A television/monitor to the right demonstrating our online ROI cost-savings calculator

Because these other booth elements will explain our products and technology in greater detail, the backdrop should NOT attempt to explain everything we do.

Its primary purpose is to stop traffic, establish the Vornelle brand, and communicate our core economic and sustainability value proposition.

Final Deliverables

The winning designer must provide artwork properly sized and positioned using our supplied 8' × 8' tension-fabric display template.

Final files should include:

Print-ready, high-resolution PDF
Editable source/vector artwork
All images embedded
Fonts converted to outlines
Artwork correctly positioned within the supplied printer template
Original Vornelle corporate logo incorporated without modification
The 3–5 Second Test

This is perhaps the most important requirement.

Someone walking down a tradeshow aisle should be able to look at the backdrop for 3–5 seconds and understand:

Vornelle offers safer, sustainable, high-performance commercial cleaning — at a lower cost.

The three offers we particularly want them to remember are:

FREE CHEMICAL ANALYSIS

SAVE UP TO 60%

AS LITTLE AS $0.27/GALLON

The overall takeaway should be:

Sustainable cleaning does not have to cost more.

We want the winning design to make that message immediately understandable, credible, and memorable.

Colors
0054AA
0677BA
7BADD7
CADEEF
E8F1F8
0094D4
00A9DD
6FCCEA
C7EBF8
E9F6FB
00AB8E
00BBA5
67D7C9
C6EFE9
E9F9F6
59FF00
82FF00
B8FF75
E3FFCB
F4FFEA

```html
<!DOCTYPE html>
<html lang="en">
<head>
<meta charset="utf-8">
<title>Vornelle — Sustainable Cleaning Backdrop</title>
<link href="https://fonts.googleapis.com/css2?family=League+Spartan:wght@500;600;700;800&display=swap" rel="stylesheet">
<style>
  :root{
    --stage:#e6e6e6;
    --navy:#1c3366;
    --navy-deep:#142a5c;
    --blue:#2f5fae;
    --blue-mid:#2a4f9a;
    --blue-wave:#3a6cc0;
    --green:#6f9f2a;
    --green-bright:#8cc63f;
    --ink:#1a1a1a;
    --white:#ffffff;
  }
  html,body{margin:0;padding:0;width:792px;height:1200px;overflow:hidden;background:var(--stage);}
  .backdrop{position:absolute;left:26px;top:230px;width:740px;height:741px;box-shadow:0 6px 18px rgba(0,0,0,.18);}
  .backdrop svg{display:block;width:100%;height:100%;font-family:"League Spartan",Arial,sans-serif;}
  .navy{fill:var(--navy);}
  .green{fill:var(--green);}
  .blue{fill:var(--blue);}
  .white{fill:var(--white);}
  .ink{fill:var(--ink);}
  .card-outline{fill:var(--white);stroke:var(--navy);stroke-width:2.5;}
  .icon-line{fill:none;stroke:var(--white);stroke-width:3;stroke-linecap:round;stroke-linejoin:round;}
  .rule-white{stroke:var(--white);stroke-width:2;}
  .rule-green{stroke:var(--green-bright);stroke-width:2;}
</style>
</head>
<body>
<div class="backdrop">
<svg viewBox="0 0 984 985" xmlns="http://www.w3.org/2000/svg">
  <defs>
    <linearGradient id="photoFade" x1="0" y1="0" x2="1" y2="0">
      <stop offset="0" stop-color="#ffffff" stop-opacity="0"/>
      <stop offset=".3" stop-color="#e9eef1" stop-opacity=".8"/>
      <stop offset="1" stop-color="#c5d2da"/>
    </linearGradient>
    <linearGradient id="photoTop" x1="0" y1="0" x2="0" y2="1">
      <stop offset="0" stop-color="#ffffff"/>
      <stop offset=".3" stop-color="#ffffff" stop-opacity=".85"/>
      <stop offset=".6" stop-color="#ffffff" stop-opacity="0"/>
    </linearGradient>
    <linearGradient id="ruleFade" x1="0" x2="1">
      <stop offset="0" stop-color="#6a9a2a"/>
      <stop offset="1" stop-color="#6a9a2a" stop-opacity="0"/>
    </linearGradient>
    <linearGradient id="navyBand" x1="0" y1="0" x2="0" y2="1">
      <stop offset="0" stop-color="#21408a"/>
      <stop offset="1" stop-color="#142a5c"/>
    </linearGradient>
    <linearGradient id="greenSwoosh" x1="0" y1="0" x2="1" y2="1">
      <stop offset="0" stop-color="#8cc63f"/>
      <stop offset="1" stop-color="#6c9e26"/>
    </linearGradient>
  </defs>

  <rect class="white" width="984" height="985"/>

  <!-- facility photo area -->
  <g role="img" aria-label="Bright modern commercial lobby corridor with glass walls, polished floor and planters">
    <rect x="430" y="0" width="554" height="640" fill="url(#photoFade)"/>
    <rect x="430" y="0" width="554" height="640" fill="url(#photoTop)"/>
  </g>

  <!-- headline -->
  <g font-weight="800">
    <text x="58" y="109" font-size="68" class="navy" textLength="511" lengthAdjust="spacingAndGlyphs">SUSTAINABLE</text>
    <text x="58" y="168" font-size="68" class="green" textLength="352" lengthAdjust="spacingAndGlyphs">CLEANING</text>
    <text x="58" y="216" font-size="38" font-weight="700" class="blue" textLength="348" lengthAdjust="spacingAndGlyphs">DOES NOT HAVE TO</text>
    <text x="56" y="280" font-size="68" class="navy" textLength="548" lengthAdjust="spacingAndGlyphs">BE EXPENSIVE.</text>
  </g>
  <rect x="58" y="310" width="460" height="3" fill="url(#ruleFade)"/>

  <!-- brand name -->
  <text x="598" y="131" font-size="62" font-weight="700" class="ink">Vornelle®</text>

  <!-- navy lower band -->
  <path d="M0,571 C110,610 220,650 360,656 C520,662 700,620 984,614 V985 H0 Z" fill="url(#navyBand)"/>

  <!-- value cards -->
  <g class="offer-free">
    <path class="card-outline" d="M41,670 V420 A78,78 0 0 1 198,420 V670"/>
    <circle cx="120" cy="404" r="60" fill="var(--navy)" stroke="var(--white)" stroke-width="3"/>
    <path class="icon-line" d="M110,378 H130 M114,378 V400 L98,430 H142 L126,400 V378 M104,418 H136"/>
    <text x="120" y="531" font-size="56" font-weight="800" text-anchor="middle" class="navy">FREE</text>
    <text x="120" y="551" font-size="15" font-weight="600" text-anchor="middle" class="blue">Cleaning</text>
    <text x="120" y="566" font-size="15" font-weight="600" text-anchor="middle" class="blue" textLength="123" lengthAdjust="spacingAndGlyphs">Chemical Analysis</text>
    <text x="120" y="584" font-size="13" font-weight="600" text-anchor="middle" class="ink">See how much</text>
    <text x="120" y="598" font-size="13" font-weight="600" text-anchor="middle" class="ink">you can save.</text>
  </g>
  <g class="offer-save">
    <path class="card-outline" d="M218,670 V420 A78,78 0 0 1 373,420 V670"/>
    <circle cx="296" cy="404" r="60" fill="var(--green)" stroke="var(--white)" stroke-width="3"/>
    <path class="icon-line" d="M267,406 H291 V432 H267 Z M279,406 V386 M279,394 L271,388 M279,394 L287,388 M299,432 V418 M309,432 V412 M319,432 V404 M297,408 L321,386 M313,386 H321 V394 M299,382 H321"/>
    <text x="296" y="529" font-size="54" font-weight="800" text-anchor="middle" class="green">SAVE</text>
    <text x="237" y="553" font-size="11" font-weight="700" class="navy">UP</text>
    <text x="237" y="564" font-size="11" font-weight="700" class="navy">TO</text>
    <text x="254" y="564" font-size="34" font-weight="800" class="navy">60%</text>
    <text x="333" y="555" font-size="8" font-weight="700" class="navy">OR</text>
    <text x="333" y="564" font-size="8" font-weight="700" class="navy">MORE</text>
    <text x="296" y="586" font-size="13" font-weight="600" text-anchor="middle" class="green">on Cleaning</text>
    <text x="296" y="599" font-size="13" font-weight="600" text-anchor="middle" class="green">Chemical Costs</text>
  </g>
  <g class="offer-price">
    <path class="card-outline" d="M394,670 V420 A78,78 0 0 1 550,420 V670"/>
    <circle cx="472" cy="404" r="60" fill="var(--blue-mid)" stroke="var(--white)" stroke-width="3"/>
    <path class="icon-line" d="M444,382 H468 M444,392 H464 M444,402 H462 M444,412 H462 M444,422 H464 M444,432 H470"/>
    <circle class="icon-line" cx="482" cy="414" r="17"/>
    <text x="482" y="421" font-size="20" font-weight="700" text-anchor="middle" class="white">$</text>
    <text x="472" y="508" font-size="19" font-weight="700" text-anchor="middle" class="navy">AS LITTLE AS</text>
    <text x="472" y="556" font-size="50" font-weight="800" text-anchor="middle" class="navy" textLength="128" lengthAdjust="spacingAndGlyphs">$0.27</text>
    <text x="472" y="591" font-size="26" font-weight="700" text-anchor="middle" class="green">/GALLON</text>
  </g>

  <!-- wave strips across card bottoms -->
  <path d="M0,620 C120,640 240,662 380,664 C520,666 700,636 984,628 V700 H0 Z" fill="url(#navyBand)"/>
  <path d="M60,628 C180,650 300,662 430,658 C540,654 620,640 700,630 C600,652 490,672 360,674 C240,676 140,656 60,628 Z" fill="var(--green-bright)"/>
  <path d="M440,654 C600,626 770,612 984,618 V626 C800,622 640,636 500,660 Z" fill="var(--blue-wave)"/>

  <!-- green swoosh -->
  <path d="M453,836 C560,760 650,650 984,621 V985 H738 C700,900 600,846 453,836 Z" fill="url(#greenSwoosh)"/>

  <!-- benefit badges -->
  <g class="benefit">
    <circle cx="103" cy="736" r="39" fill="var(--green-bright)"/>
    <path class="icon-line" d="M103,714 L121,721 V736 C121,748 112,756 103,760 C94,756 85,748 85,736 V721 Z M95,737 L101,743 L112,730"/>
    <line class="rule-green" x1="64" y1="789" x2="142" y2="789"/>
    <text x="103" y="802" font-size="11" font-weight="700" text-anchor="middle" class="white">SAFER FOR</text>
    <text x="103" y="814" font-size="11" font-weight="700" text-anchor="middle" class="white">PEOPLE AND</text>
    <text x="103" y="826" font-size="11" font-weight="700" text-anchor="middle" class="white">FACILITIES</text>
    <line class="rule-green" x1="64" y1="836" x2="142" y2="836"/>
  </g>
  <g class="benefit">
    <circle cx="246" cy="736" r="39" fill="var(--green-bright)"/>
    <path class="icon-line" d="M246,758 V720 M246,740 C236,740 228,732 228,720 C238,720 246,728 246,740 M246,740 C256,740 264,732 264,720 C254,720 246,728 246,740 M246,730 C240,724 240,716 246,710 C252,716 252,724 246,730"/>
    <line class="rule-green" x1="207" y1="789" x2="285" y2="789"/>
    <text x="246" y="802" font-size="11" font-weight="700" text-anchor="middle" class="white">BETTER</text>
    <text x="246" y="814" font-size="11" font-weight="700" text-anchor="middle" class="white">FOR THE</text>
    <text x="246" y="826" font-size="11" font-weight="700" text-anchor="middle" class="white">ENVIRONMENT</text>
    <line class="rule-green" x1="207" y1="836" x2="285" y2="836"/>
  </g>
  <g class="benefit">
    <circle cx="390" cy="736" r="39" fill="var(--green-bright)"/>
    <path class="icon-line" d="M388,714 C380,726 374,734 374,743 C374,751 380,757 388,757 C396,757 402,751 402,743 C402,734 396,726 388,714 Z M398,718 C396,722 394,725 394,728 C394,731 396,733 398,733 C400,733 402,731 402,728 C402,725 400,722 398,718 Z"/>
    <line class="rule-green" x1="351" y1="789" x2="429" y2="789"/>
    <text x="390" y="802" font-size="11" font-weight="700" text-anchor="middle" class="white">BETTER</text>
    <text x="390" y="814" font-size="11" font-weight="700" text-anchor="middle" class="white">FOR YOUR</text>
    <text x="390" y="826" font-size="11" font-weight="700" text-anchor="middle" class="white">BOTTOM LINE</text>
    <line class="rule-green" x1="351" y1="836" x2="429" y2="836"/>
  </g>

  <text x="68" y="894" font-size="44" font-weight="800" class="white" textLength="367" lengthAdjust="spacingAndGlyphs">www.vornelle.com</text>

  <!-- secondary message -->
  <g class="smarter">
    <text x="778" y="741" font-size="56" font-weight="800" text-anchor="middle" class="white" textLength="260" lengthAdjust="spacingAndGlyphs">SMARTER</text>
    <text x="780" y="796" font-size="56" font-weight="800" text-anchor="middle" class="navy" textLength="287" lengthAdjust="spacingAndGlyphs">CLEANING</text>
    <line class="rule-white" x1="636" y1="807" x2="922" y2="807"/>
    <text x="778" y="839" font-size="25" font-weight="700" text-anchor="middle" class="white" textLength="276" lengthAdjust="spacingAndGlyphs">HIGH PERFORMANCE.</text>
    <text x="778" y="866" font-size="25" font-weight="700" text-anchor="middle" class="white" textLength="236" lengthAdjust="spacingAndGlyphs">LOW COST. SAFER.</text>
    <line class="rule-white" x1="636" y1="879" x2="922" y2="879"/>
  </g>
</svg>
</div>
</body>
</html>
```